Brightvale Job Specifications

Pls create α professional Job Spec for the Services Agents Role for Brightvale so it looks professional for New Hires.

Target Market(s)

Company Employees

Requirements
Must have
• Professional look

```html
<!DOCTYPE html>
<html lang="en">
<head>
<meta charset="utf-8">
<title>Brightvale – Goals, Responsibilities and Accountability</title>
<link href="https://fonts.googleapis.com/css2?family=Arimo:wght@400;700&family=Bebas+Neue&display=swap" rel="stylesheet">
<style>
  :root {
    --navy: #1d3f6e;
    --orange: #f15a24;
    --ink: #1a1a1a;
    --rule: #9a9a9a;
    --paper: #ffffff;
  }
  * { margin: 0; padding: 0; box-sizing: border-box; }
  html, body { width: 1200px; height: 848px; overflow: hidden; background: var(--paper); }
  .sheet {
    position: relative;
    width: 1200px;
    height: 848px;
    overflow: hidden;
    background: var(--paper);
    font-family: "Arimo", "Helvetica Neue", Arial, sans-serif;
    color: var(--ink);
  }
  .corner-shape {
    position: absolute;
    top: 0;
    left: 0;
  }
  .brand {
    position: absolute;
    top: 48px;
    left: 486px;
    display: flex;
    align-items: center;
    gap: 10px;
  }
  .brand-dot {
    width: 30px;
    height: 30px;
    border-radius: 50%;
    background: var(--navy);
  }
  .brand-name {
    font-family: "Arimo", "Helvetica Neue", Arial, sans-serif;
    font-weight: 700;
    font-size: 32px;
    color: var(--navy);
    letter-spacing: 0.2px;
  }
  .page-title {
    position: absolute;
    top: 112px;
    left: 114px;
    font-family: "Bebas Neue", "Oswald", sans-serif;
    font-weight: 400;
    font-size: 37px;
    line-height: 1;
    color: var(--orange);
    letter-spacing: 0.1px;
  }
  .spec-table {
    position: absolute;
    top: 166px;
    left: 115px;
    width: 971px;
    border-collapse: collapse;
    border: 1.5px solid var(--ink);
    background: var(--paper);
    font-size: 13.6px;
    line-height: 17px;
  }
  .spec-table td {
    border: 1px solid var(--rule);
    vertical-align: top;
    padding: 6px 6px 4px;
  }
  .spec-table .area { width: 259px; font-weight: 700; }
  .spec-table .area span { font-weight: 400; display: block; }
  .spec-table .goal { width: 441px; }
  .spec-table .goal b { font-weight: 700; }
  .spec-table .range { display: block; font-weight: 700; margin-top: 8px; }
  .spec-table .rating { width: 271px; }
  .rating-scale {
    display: block;
    font-family: "Bebas Neue", "Oswald", sans-serif;
    font-size: 31px;
    line-height: 30px;
    margin-top: 4px;
    color: var(--ink);
  }
  .r1 td { height: 61px; }
  .r2 td { height: 61px; }
  .r3 td { height: 61px; }
  .r4 td { height: 68px; }
  .r5 td { height: 60px; }
  .r6 td { height: 61px; }
  .r7 td { height: 61px; }
  .r8 td { height: 67px; }
  .r9 td { height: 68px; }
</style>
</head>
<body>
<main class="sheet">
  <svg class="corner-shape" width="1200" height="848" viewBox="0 0 1200 848" aria-hidden="true">
    <circle cx="1120" cy="210" r="250" fill="var(--navy)"/>
    <rect x="1070" y="115" width="50" height="50" fill="var(--orange)"/>
  </svg>

  <header class="brand">
    <span class="brand-dot"></span>
    <span class="brand-name">Brightvale</span>
  </header>

  <h1 class="page-title">Goals, Responsibilities and Accountability</h1>

  <table class="spec-table">
    <tr class="r1">
      <td class="area">High Quality Results.<span>Delivery of high quality focused results across Crest Cleaning Services.</span></td>
      <td class="goal"><b>Goal:</b> High Quality results for each service<br>performed. Expected Rating: 100/100</td>
      <td class="rating">Rating of Performance:<span class="rating-scale">1- 5</span></td>
    </tr>
    <tr class="r2">
      <td class="area">Service, Customer Service and Communication Skills</td>
      <td class="goal"><b>Goal:</b> Building positive working relationships on site with customers and Team Members. Rating range 90 – 100 %</td>
      <td class="rating">Rating of Performance:<span class="rating-scale">1- 5</span></td>
    </tr>
    <tr class="r3">
      <td class="area">Positive Attitude</td>
      <td class="goal"><b>Goal:</b> Building great positive relationships with Team Members, Management and Customers. Rating range 90 – 100 %</td>
      <td class="rating">Rating of Performance:<span class="rating-scale">1- 5</span></td>
    </tr>
    <tr class="r4">
      <td class="area">Technical Skills</td>
      <td class="goal"><b>Goal:</b> Expert in Equipment Cleaning. Use of Gurney Skills, and Thorough Skills on Detailed Commercial Cleaning Services.<span class="range">Range 1 – 5, 5 being highly effective.</span></td>
      <td class="rating">Rating of Performance:<span class="rating-scale">1- 5</span></td>
    </tr>
    <tr class="r5">
      <td class="area">Knowledge of Standard Procedures</td>
      <td class="goal"><b>Goal:</b> Learning all Brightvale standard operating procedures.<span class="range" style="margin-top:16px">Range 1 – 5, 5 being highly effective.</span></td>
      <td class="rating">Rating of Performance:<span class="rating-scale">1- 5</span></td>
    </tr>
    <tr class="r6">
      <td class="area">Reporting on JobTrak correctly</td>
      <td class="goal"><b>Goal:</b> 100 % reporting effectively on JobTrak</td>
      <td class="rating">Rating of Performance:<span class="rating-scale">1- 5</span></td>
    </tr>
    <tr class="r7">
      <td class="area">Sales and Marketing</td>
      <td class="goal"><b>Goal:</b> Upselling of Brightvale Services with Marketing Brochures.<span class="range" style="margin-top:16px">Range 1 – 5, 5 being highly effective.</span></td>
      <td class="rating">Rating of Performance:<span class="rating-scale">1- 5</span></td>
    </tr>
    <tr class="r8">
      <td class="area">Safety Awareness and Application</td>
      <td class="goal"><b>Goal:</b> Full compliance with all Safety and Risk<br>Assessments completed.<span class="range">Range 1 – 5, 5 being highly effective.</span></td>
      <td class="rating">Rating of Performance:<span class="rating-scale">1- 5</span></td>
    </tr>
    <tr class="r9">
      <td class="area">Problem Solving Ability</td>
      <td class="goal"><b>Goal:</b> Find positive solutions to any challenges in<br>the workplace.<span class="range">Range 1 – 5, 5 being highly effective.</span></td>
      <td class="rating">Rating of Performance:<span class="rating-scale">1- 5</span></td>
    </tr>
  </table>
</main>
</body>
</html>
```